Vantrel

I already have a website created through Plovix.com - https://vantrel.co.nz.

Its an accounting services business, can get ideas from tzhl.co.nz, fwu.co.nz, yrx.co.nz

I would like to have this recreated using coding. I need the following features and functionalities incorporated:

- Live Chat feature
- Moving Carousel feature for Reviews
- Advanced SEO support (Google Analytics)

Industry/Entity Type

accounting

Coding

Coded - Design and coding required

Number of Pages Required

5+ page

```html
<!DOCTYPE html>
<html lang="en">
<head>
<meta charset="utf-8">
<title>Vantrel – Chartered Accountant</title>
<link rel="stylesheet" href="https://fonts.googleapis.com/css2?family=Poppins:wght@400;500;600&display=swap">
<style>
:root{
  --dark:#3a4846;
  --dark-2:#2f3b39;
  --mint:#9fd5c3;
  --ink:#1f2624;
  --muted:#4a4f4e;
  --light:#ececec;
  --panel:#ffffff;
  --gold:#f0c23a;
}
*{box-sizing:border-box;margin:0;padding:0}
html,body{width:1200px;height:4971px;overflow:hidden}
body{font-family:"Poppins",sans-serif;color:var(--ink);background:#fff;position:relative}
.abs{position:absolute}
.btn{position:absolute;background:var(--dark);color:#fff;font-size:17px;font-weight:500;display:flex;align-items:center;justify-content:center;border-radius:10px;text-transform:uppercase}
.photo{position:absolute}
/* header */
.site-header{position:absolute;left:0;top:0;width:1200px;height:148px;background:var(--dark)}
.brand{position:absolute;display:flex;flex-direction:column;align-items:center;color:var(--mint);font-weight:600;letter-spacing:5px}
.brand .mark{border:9px solid var(--mint);border-radius:50%}
.nav{position:absolute;left:520px;top:64px;display:flex;gap:28px;font-size:14px;color:#fff}
.nav a{color:#fff;text-decoration:none}
.nav .active{font-weight:600}
.chat-btn{position:absolute;left:970px;top:55px;width:163px;height:39px;background:#fff;border-radius:8px;display:flex;align-items:center;justify-content:center;gap:8px;font-size:15px;font-weight:600;color:var(--dark)}
/* hero */
.hero{position:absolute;left:0;top:148px;width:1200px;height:559px;background:linear-gradient(90deg,#f2f2f2 0%,#ececec 45%,#c9c3bb 70%,#a9a29a 100%)}
.hero h1{position:absolute;left:70px;top:72px;font-size:57px;line-height:60px;font-weight:500;color:var(--ink)}
.hero p{position:absolute;left:70px;top:336px;width:560px;font-size:13.5px;line-height:24px}
/* features */
.feature{position:absolute;width:260px;text-align:center;font-size:14px;font-weight:500}
.feature .ring{width:178px;height:178px;border-radius:50%;background:var(--dark);margin:0 auto 22px;border:6px solid #cfcfcf;box-shadow:0 0 0 3px var(--dark) inset;display:flex;align-items:center;justify-content:center}
/* section heads */
.sec-title{position:absolute;font-size:42px;font-weight:500;text-transform:uppercase;color:var(--ink)}
.sec-sub{position:absolute;font-size:15px;font-weight:600;display:flex;align-items:center;gap:8px}
.sec-sub i{display:block;width:40px;height:2px;background:var(--ink)}
/* cards */
.card{position:absolute;top:1270px;width:335px;height:430px;background:var(--panel);box-shadow:0 2px 12px rgba(0,0,0,.12);text-align:center}
.card .pic{position:absolute;left:27px;top:28px;width:281px;height:197px;border-radius:6px}
.card h3{position:absolute;top:256px;width:100%;font-size:23px;font-weight:500}
.card p{position:absolute;left:30px;top:298px;width:275px;font-size:13.5px;line-height:27px}
.card .btn{left:91px;top:407px;width:152px;height:46px;border-radius:8px}
/* cta */
.cta{position:absolute;left:0;top:1915px;width:1200px;height:480px;background:var(--light)}
.cta h2{position:absolute;left:545px;top:80px;font-size:40px;line-height:48px;font-weight:500;text-transform:uppercase}
.cta p{position:absolute;left:555px;top:290px;font-size:15.5px}
/* about */
.about-lead{position:absolute;left:100px;top:2626px;width:500px;font-size:18.5px;line-height:26px;font-weight:500;text-align:justify}
.about-body{position:absolute;left:100px;top:2716px;width:500px;font-size:13.5px;line-height:22.5px}
/* testimonials */
.testi{position:absolute;left:0;top:3145px;width:1200px;height:588px;background:linear-gradient(90deg,#e6e6e3,#f0efec 40%,#ecebe4 70%,#e8e3c9)}
.testi .quote{position:absolute;left:245px;top:356px;width:710px;text-align:center;font-size:16px;line-height:29px}
/* contact */
.field{position:absolute;height:45px;background:#fff;border:1px solid #e0e0e0;box-shadow:0 1px 5px rgba(0,0,0,.1);font-size:13px;color:#888;padding:14px 20px}
/* footer */
.site-footer{position:absolute;left:0;top:4447px;width:1200px;height:524px;background:var(--dark);color:#fff}
.site-footer h4{position:absolute;font-size:23px;font-weight:500}
.flink{position:absolute;left:508px;font-size:15px;display:flex;align-items:center;gap:12px}
.flink i{width:12px;height:12px;border-radius:50%;background:#fff;display:block}
.fcontact{position:absolute;left:781px;display:flex;align-items:flex-start;gap:14px;font-size:15px;line-height:25px}
.fcontact .ic{width:36px;height:36px;border-radius:50%;background:#fff;display:flex;align-items:center;justify-content:center;flex:none}
</style>
</head>
<body>

<header class="site-header">
  <div class="brand" style="left:70px;top:14px;font-size:22px">
    <div class="mark" style="width:80px;height:80px;margin-bottom:10px"></div>VANTREL
  </div>
  <nav class="nav">
    <a class="active" href="#">HOME</a><a href="#">SERVICES</a><a href="#">ABOUT US</a><a href="#">PRICING</a><a href="#">CONTACT US</a>
  </nav>
  <div class="chat-btn">
    <svg width="34" height="26" viewBox="0 0 34 26"><ellipse cx="17" cy="13" rx="16" ry="12" fill="var(--dark)"/><circle cx="11" cy="13" r="2" fill="#fff"/><circle cx="17" cy="13" r="2" fill="#fff"/><circle cx="23" cy="13" r="2" fill="#fff"/></svg>LIVE CHAT
  </div>
</header>

<section class="hero">
  <div class="photo" role="img" aria-label="Team of accountants reviewing work at a laptop" style="left:560px;top:0;width:640px;height:559px;background:linear-gradient(160deg,#e9e4dc 0%,#c7b8a5 45%,#8fa3b6 100%)"></div>
  <h1>WE EMPOWER<br>BUSINESSES<br>LEDGR CERTIFIED,<br>RESULTS DRIVEN</h1>
  <p>A Chartered Accountant with in-depth professional experience across New Zealand's diverse financial landscape.</p>
  <div class="btn" style="left:70px;top:415px;width:180px;height:54px;border-radius:27px;font-size:17px">GET STARTED</div>
</section>

<div class="feature" style="left:108px;top:777px">
  <div class="ring"><svg width="70" height="70" viewBox="0 0 70 70" fill="none" stroke="#fff" stroke-width="3"><path d="M12 60V40M26 60V28M40 60V34M54 60V18"/><path d="M8 62h54"/></svg></div>Tailored Financial Solutions
</div>
<div class="feature" style="left:466px;top:777px">
  <div class="ring"><div style="width:76px;height:76px;border-radius:50%;background:#fff"></div></div>Ledgr Advisor Certified
</div>
<div class="feature" style="left:824px;top:777px">
  <div class="ring"><svg width="70" height="70" viewBox="0 0 70 70" fill="none" stroke="#fff" stroke-width="3"><path d="M10 58L26 42L38 50L60 22"/><path d="M50 22h10v10"/><path d="M8 62h54"/></svg></div>Enhanced Financial Clarity
</div>

<h2 class="sec-title" style="left:0;width:1200px;text-align:center;top:1122px">OUR SERVICES</h2>
<div class="sec-sub" style="left:500px;top:1177px;width:200px;justify-content:center"><i></i>WHAT WE DO<i></i></div>

<article class="card" style="left:74px">
  <div class="pic" role="img" aria-label="Printed financial reports with charts" style="background:linear-gradient(135deg,#f1f1f4,#c7c2e4 50%,#6e8a54)"></div>
  <h3>MONTHLY REPORTING</h3>
  <p>Regular, detailed financial reports that give you a clear view of your financial position at all times.</p>
  <div class="btn">READ MORE</div>
</article>
<article class="card" style="left:432px">
  <div class="pic" role="img" aria-label="Laptop and tablet showing cash flow charts" style="background:linear-gradient(135deg,#d8a664,#5d5a5e 50%,#2b4c7a)"></div>
  <h3>CASH FLOW REPORTING</h3>
  <p>Accurate forecasting and monitoring of your cash flow to ensure liquidity and financial stability.</p>
  <div class="btn">READ MORE</div>
</article>
<article class="card" style="left:798px">
  <div class="pic" role="img" aria-label="Hand on a tablet with tax figures" style="background:linear-gradient(135deg,#0f2446,#2d5390 50%,#d7802e)"></div>
  <h3>GST, PAYE</h3>
  <p>Compliance with GST &amp; PAYE requirements, including accurate calculations, filings, and advice.</p>
  <div class="btn">READ MORE</div>
</article>

<svg class="abs" style="left:578px;top:1783px" width="46" height="10"><circle cx="5" cy="5" r="4" fill="var(--ink)"/><circle cx="14" cy="5" r="3.5" fill="none" stroke="var(--ink)"/><circle cx="23" cy="5" r="3.5" fill="none" stroke="var(--ink)"/><circle cx="32" cy="5" r="3.5" fill="none" stroke="var(--ink)"/><circle cx="41" cy="5" r="3.5" fill="none" stroke="var(--ink)"/></svg>

<section class="cta">
  <div class="photo" role="img" aria-label="Two smiling colleagues working on a laptop" style="left:0;top:0;width:540px;height:480px;border-radius:0 480px 480px 0;background:linear-gradient(120deg,#d9d6cf,#b49a7b 45%,#d6b84e 80%)"></div>
  <h2>LET VANTREL BE THE<br>CORNERSTONE OF YOUR<br>FINANCIAL STABILITY AND<br>GROWTH.</h2>
  <p>Contact us today to learn how we can empower your organization.</p>
  <div class="btn" style="left:557px;top:334px;width:185px;height:56px;font-size:18px">CONTACT US</div>
</section>

<h2 class="sec-title" style="left:100px;top:2532px">ABOUT US</h2>
<div class="sec-sub" style="left:100px;top:2587px">WHO WE ARE<i></i></div>
<p class="about-lead">A Chartered Accountant with in-depth professional experience across New Zealand's diverse financial landscape.</p>
<p class="about-body">Throughout my career I have had the privilege of working across various sectors, including commercial organisations, charitable trusts and for purpose organisations, government-funded entities, as well as the health, disability, and education sectors.</p>
<div class="abs" style="left:100px;top:2822px;font-size:21px;font-weight:500">Mariam</div>
<div class="abs" style="left:100px;top:2849px;font-size:12.5px">BCom, GradDip, CA</div>
<div class="btn" style="left:100px;top:2892px;width:172px;height:60px;font-size:15px">KNOW MORE</div>
<div class="abs" style="left:655px;top:2510px;width:474px;height:474px;border-radius:50%;border:2px solid var(--ink)"></div>
<div class="photo" role="img" aria-label="Portrait of the principal accountant" style="left:664px;top:2519px;width:456px;height:456px;border-radius:50%;background:linear-gradient(160deg,#5b615e,#3e423f 50%,#c9c6c0)"></div>
<div class="abs" style="left:624px;top:2832px;width:186px;height:186px;border-radius:50%;background:var(--dark)"></div>
<div class="brand" style="left:624px;top:2872px;width:186px;font-size:16px;letter-spacing:4px">
  <div class="mark" style="width:58px;height:58px;border-width:6px;margin-bottom:10px"></div>VANTREL
</div>

<section class="testi">
  <div class="photo" role="img" aria-label="Faded office scene with colleagues at work" style="left:0;top:0;width:1200px;height:588px;background:linear-gradient(90deg,rgba(160,150,140,.25),rgba(255,255,255,0) 50%,rgba(210,190,90,.25));"></div>
  <h2 class="sec-title" style="left:0;width:1200px;text-align:center;top:83px">OUR TESTIMONIALS</h2>
  <div class="sec-sub" style="left:480px;top:137px;width:240px;justify-content:center"><i></i>CLIENT REVIEWS<i></i></div>
  <svg class="abs" style="left:552px;top:242px" width="96" height="76" viewBox="0 0 96 76" fill="var(--dark)"><path d="M0 40Q0 6 34 0v12Q18 18 18 34h20v42H0z"/><path d="M54 40Q54 6 88 0v12Q72 18 72 34h22v42H54z"/></svg>
  <p class="quote">Lorem ipsum dolor sit amet, consectetur adipiscing elit, sed do eiusmod tempor<br>incididunt ut labore et dolore magna aliqua. Ut enim ad minim veniam, quis nostrud<br>exercitation ullamco laboris .</p>
  <div class="abs" style="left:0;width:1200px;text-align:center;top:474px;font-size:21px;font-weight:500">DANIEL HART</div>
  <div class="abs" style="left:0;width:1200px;text-align:center;top:502px;font-size:26px;letter-spacing:5px;color:var(--gold)">★★★★★</div>
  <svg class="abs" style="left:152px;top:372px" width="22" height="34" fill="none" stroke="var(--ink)" stroke-width="4"><path d="M18 3L4 17l14 14"/></svg>
  <svg class="abs" style="left:1026px;top:372px" width="22" height="34" fill="none" stroke="var(--ink)" stroke-width="4"><path d="M4 3l14 14L4 31"/></svg>
</section>

<h2 class="sec-title" style="left:98px;top:3890px">CONTACT US</h2>
<div class="sec-sub" style="left:100px;top:3945px">GET IN TOUCH<i></i></div>
<div class="field" style="left:96px;top:3995px;width:221px">First Name:</div>
<div class="field" style="left:337px;top:3995px;width:221px">Last Name:</div>
<div class="field" style="left:96px;top:4060px;width:221px">Phone:</div>
<div class="field" style="left:337px;top:4060px;width:221px">Email:</div>
<div class="field" style="left:96px;top:4125px;width:462px;height:143px">Mesage:</div>
<div class="btn" style="left:93px;top:4303px;width:184px;height:58px;font-size:19px;font-weight:600;text-transform:none">SUBMIT NOW</div>
<div class="photo" role="img" aria-label="Smiling businesswoman at a laptop with colleagues behind" style="left:635px;top:3930px;width:470px;height:470px;border-radius:50%;background:linear-gradient(150deg,#e8ecef,#aab6bf 50%,#3c3632)"></div>

<footer class="site-footer">
  <div class="brand" style="left:140px;top:126px;width:200px;font-size:28px;letter-spacing:6px">
    <div class="mark" style="width:100px;height:100px;border-width:11px;margin-bottom:14px"></div>VANTREL
  </div>
  <svg class="abs" style="left:175px;top:316px" width="120" height="32"><circle cx="17" cy="16" r="15" fill="#fff"/><circle cx="54" cy="16" r="15" fill="#fff"/><circle cx="91" cy="16" r="15" fill="#fff"/></svg>
  <h4 style="left:508px;top:145px">LINKS</h4>
  <div class="abs" style="left:508px;top:182px;width:50px;height:2px;background:#fff"></div>
  <div class="flink" style="top:212px"><i></i>Services</div>
  <div class="flink" style="top:245px"><i></i>Avout US</div>
  <div class="flink" style="top:278px"><i></i>Pricing</div>
  <div class="flink" style="top:311px"><i></i>Contact Us</div>
  <h4 style="left:781px;top:145px">CONTACT US</h4>
  <div class="fcontact" style="top:223px"><span class="ic"><svg width="18" height="18" viewBox="0 0 24 24" fill="var(--dark)"><path d="M6.6 10.8a15 15 0 006.6 6.6l2.2-2.2a1 1 0 011-.3 11 11 0 003.6.6 1 1 0 011 1V20a1 1 0 01-1 1A17 17 0 013 4a1 1 0 011-1h3.5a1 1 0 011 1 11 11 0 00.6 3.6 1 1 0 01-.3 1z"/></svg></span><span style="padding-top:5px">021555014</span></div>
  <div class="fcontact" style="top:280px"><span class="ic"><svg width="18" height="14" viewBox="0 0 18 14" fill="var(--dark)"><path d="M0 0h18v14H0z"/><path d="M1 1l8 6 8-6" stroke="#fff" stroke-width="1.5" fill="none"/></svg></span><span style="padding-top:5px">contact@vantrel.co.nz</span></div>
  <div class="fcontact" style="top:333px"><span class="ic"><svg width="16" height="20" viewBox="0 0 16 20" fill="var(--dark)"><path d="M8 0a8 8 0 018 8c0 6-8 12-8 12S0 14 0 8a8 8 0 018-8z"/><circle cx="8" cy="8" r="3" fill="#fff"/></svg></span><span>Lorem ipsum dolor,Lorem ipsum dolor,<br>Lorem ipsum dolor.</span></div>
  <div class="abs" style="left:72px;top:438px;width:1066px;height:1px;background:rgba(255,255,255,.4)"></div>
  <div class="abs" style="left:0;width:1200px;text-align:center;top:474px;font-size:14px">© 2025. All Rights Reserved.</div>
</footer>

</body>
</html>
```